New south Australia high-end red wine label & logo design

Marvick Estate exports premium south Australian wine to oversea market. We are looking for a professional graphic designer to design a full set of wine label and logo for our new red wine, the label & logo should look 'high-end' & Luxury and attractive. Black & gold color is preferred. I have attached example images to demonstrate the feel that we are looking for. These are just a possible starting point. The expectation is that the label would be professional/polished. I am open to any and all designs that would alter my perception of what will be best!

Target customer -

we need the label to be print-ready.

There will be 3 parts to this design.

Top Cover design with gold text wrapped, the front label and the back label

-Brand name Marvik Estate
-text wine of Australia
-text Cabernet
-Year 2015
-text Sourced from premium Australian wine growing region Merrigal valley

Look and Feel:
• Elegant
• Serious
• Modern/Traditional
• Professional
• Gender Neutral
• Upmarket

--------------Back Label text---------------
Rich and opulent with intense fruit aromas of black berry, liquorice and cassis with hints of dark chocolate and pungent spices. Sumptuous and textured palate with beautifully detailed ripe black fruits flowing seamlessly across the palate. French oak provides a complex harmony and finish of great length, balance and purity.

Produced by Rolk Haven Group International Pty Ltd
27 Fellmore Road,Quandip, South Australia, 5172
14.5 ALC/VOL
Wine of Australia
Approx 8.3 Standard Drinks
Contains Sulphites
750 ML
Please leave the space for Bar Code

Requirements
Must have
• wine name, wine logo, wine type etc (should include all 'must-have the required fields wine lable)
Nice to have
• Desginer's own idea
Should not have
• should not be too playful

```html
<!DOCTYPE html>
<html lang="en">
<head>
<meta charset="utf-8">
<title>Marvik Estate – Cabernet Sauvignon 2015 Label</title>
<link href="https://fonts.googleapis.com/css2?family=Playfair+Display:wght@400;700;900&family=Italianno&display=swap" rel="stylesheet">
<style>
  :root {
    --paper: #ffffff;
    --label-black: #212121;
    --cream: #f8f2dd;
    --gold: #d4a93a;
    --gold-light: #f2d57a;
    --gold-dark: #8c6516;
    --white: #ffffff;
  }
  * { margin: 0; padding: 0; box-sizing: border-box; }
  html, body {
    width: 1019px;
    height: 1200px;
    overflow: hidden;
    background: var(--paper);
  }
  .canvas {
    position: relative;
    width: 1019px;
    height: 1200px;
    background: var(--paper);
  }
  .label {
    position: absolute;
    left: 132px;
    top: 136px;
    width: 755px;
    height: 909px;
    background: var(--label-black);
  }
  .brand-seal {
    position: absolute;
    left: 311px;
    top: 49px;
    width: 132px;
    height: 132px;
    border: 2px solid var(--gold);
    border-radius: 50%;
    display: flex;
    align-items: center;
    justify-content: center;
    text-align: center;
    font-family: "Playfair Display", serif;
    font-weight: 700;
    font-size: 15px;
    letter-spacing: 2px;
    line-height: 1.3;
    color: var(--gold);
  }
  .brand-name {
    position: absolute;
    left: 0;
    width: 100%;
    top: 215px;
    text-align: center;
    font-family: "Playfair Display", serif;
    font-weight: 900;
    font-size: 64px;
    letter-spacing: 4px;
    padding-left: 4px;
    line-height: 1;
    color: var(--cream);
  }
  .varietal {
    position: absolute;
    left: 0;
    width: 100%;
    top: 301px;
    text-align: center;
    font-family: "Playfair Display", serif;
    font-weight: 400;
    font-size: 20px;
    line-height: 1;
    letter-spacing: 10px;
    padding-left: 10px;
    color: var(--cream);
  }
  .vintage {
    position: absolute;
    z-index: 2;
    left: 0;
    width: 100%;
    top: 405px;
    text-align: center;
    font-family: "Playfair Display", serif;
    font-weight: 400;
    font-size: 32px;
    font-variant-numeric: lining-nums;
    letter-spacing: 4px;
    padding-left: 4px;
    line-height: 36px;
    color: var(--white);
  }
  .lyre-illustration {
    position: absolute;
    z-index: 1;
    left: 272px;
    top: 474px;
    width: 210px;
    height: 270px;
    border-radius: 40% 40% 46% 46% / 30% 30% 50% 50%;
    background: linear-gradient(160deg, var(--gold-light) 0%, var(--gold) 45%, var(--gold-dark) 100%);
    opacity: 0.9;
  }
  .origin {
    position: absolute;
    left: 0;
    width: 100%;
    top: 806px;
    text-align: center;
    font-family: "Italianno", cursive;
    font-size: 66px;
    line-height: 1;
    color: var(--white);
  }
</style>
</head>
<body>
  <main class="canvas">
    <section class="label">
      <div class="brand-seal">MARVIK<br>ESTATE</div>
      <h1 class="brand-name">MARVIK ESTATE</h1>
      <p class="varietal">CABERNET SAUVIGNON</p>
      <p class="vintage">20<br>15</p>
      <div class="lyre-illustration" role="img" aria-label="Gold foil engraving of a classical lyre on a pedestal"></div>
      <p class="origin">Wine of Australia</p>
    </section>
  </main>
</body>
</html>
```